Enterprise image desing

The designs are for a fashion store for young men and women.
Updates

Los diseƱos parecen similares

Target Market(s)

Young

Font styles to use
Sans Serif

Colors
ec1f27
ffffff
1b1b1b

Requirements
Must have
• Use clean and modern sources
Nice to have
• n / a
Should not have
• n / a

```html
<!DOCTYPE html>
<html lang="es">
<head>
<meta charset="utf-8">
<title>Korvalen – Identidad corporativa</title>
<link href="https://fonts.googleapis.com/css2?family=Poppins:wght@600&family=Arimo:wght@400;700&display=swap" rel="stylesheet">
<style>
  :root{
    --dark:#1b1b1b;
    --dark-soft:#2d2d2d;
    --red:#ec1f27;
    --paper:#f3f3f3;
    --ink:#1b1b1b;
    --white:#ffffff;
    --bg:#e3e3e3;
  }
  *{box-sizing:border-box;margin:0;padding:0}
  html,body{width:1200px;height:800px;overflow:hidden;background:var(--bg)}
  body{position:relative;font-family:"Arimo",Arial,sans-serif;color:var(--ink)}
  .piece{position:absolute;overflow:hidden;box-shadow:0 1px 3px rgba(0,0,0,.12)}
  .brand{display:flex;align-items:center;gap:.35em;font-family:"Poppins",sans-serif;font-weight:600;letter-spacing:.02em;line-height:1;color:var(--dark);white-space:nowrap}
  .brand::before{content:"";width:.8em;height:.8em;background:var(--red);flex:none}
  .brand--light{color:var(--white)}
  .brand--light::before{background:var(--white)}
  .bars{position:absolute;left:0;top:0;right:0;display:flex}
  .bars .bar-dark{background:var(--dark);flex:0 0 70%}
  .bars .bar-red{background:var(--red);flex:1;margin-left:2px}
  .contact{list-style:none;line-height:1.4;white-space:nowrap}
  .contact li{display:flex;align-items:center;gap:3px}
  .contact li::before{content:"";width:.8em;height:.8em;border:1px solid var(--red);border-radius:50%;flex:none}
  .contact--right li{flex-direction:row-reverse}

  /* Folder */
  .folder{left:261px;top:94px;width:319px;height:433px;background:var(--dark)}
  .folder .brand{position:absolute;left:0;right:0;top:59px;justify-content:center;font-size:31px}
  .folder-panel{position:absolute;left:0;right:0;bottom:0;height:293px;background:var(--dark-soft)}

  /* Letterhead */
  .letterhead{left:626px;top:94px;width:291px;height:414px;background:var(--paper)}
  .letterhead .bars{height:8px}
  .letterhead .brand{position:absolute;left:27px;top:24px;font-size:19px}
  .letterhead .contact{position:absolute;left:205px;top:24px;font-size:5.4px}
  .letterhead-foot{position:absolute;left:53px;right:50px;top:394px;border-top:1px solid var(--red);padding-top:2px;font-size:6px;text-align:center;white-space:nowrap}

  /* Envelope front */
  .envelope-front{left:124px;top:556px;width:358px;height:157px;background:var(--paper)}
  .envelope-front .bars{height:7px}
  .envelope-front .brand{position:absolute;left:19px;top:24px;font-size:20px}
  .envelope-address{position:absolute;left:19px;top:117px;font-size:5.3px;line-height:1.2;white-space:nowrap;padding-bottom:2px;border-bottom:1px solid var(--red)}
  .envelope-front .contact{position:absolute;left:19px;top:130px;font-size:5.4px}

  /* Envelope back */
  .envelope-back{left:519px;top:556px;width:359px;height:157px;background:var(--paper)}
  .envelope-back svg{position:absolute;left:0;top:0}

  /* Business card front */
  .card-front{left:915px;top:519px;width:168px;height:97px;background:var(--dark);color:var(--white)}
  .card-front .brand{position:absolute;left:0;right:0;top:38px;justify-content:center;font-size:14px}
  .card-front-info{position:absolute;left:0;right:0;top:73px;font-size:4.4px;line-height:1.6;text-align:center;white-space:nowrap}

  /* Business card back */
  .card-back{left:915px;top:641px;width:168px;height:100px;background:var(--paper)}
  .card-back .bars{height:6px}
  .card-back .brand{position:absolute;left:10px;top:19px;font-size:11px}
  .card-person{position:absolute;right:9px;top:48px;text-align:right;font-size:5.2px;line-height:1.2}
  .card-person strong{display:block;font-weight:700}
  .card-rule{position:absolute;left:8px;right:48px;top:57px;border-top:1px solid var(--red);opacity:.6}
  .card-back .contact{position:absolute;right:9px;top:66px;font-size:4.4px}
  .card-back-address{position:absolute;left:9px;top:82px;font-size:4.4px;line-height:1.3;width:72px}
</style>
</head>
<body>

  <section class="piece folder" aria-label="Carpeta">
    <div class="brand brand--light">KORVALEN</div>
    <div class="folder-panel"></div>
  </section>

  <section class="piece letterhead" aria-label="Hoja membretada">
    <div class="bars"><span class="bar-dark"></span><span class="bar-red"></span></div>
    <div class="brand">KORVALEN</div>
    <ul class="contact">
      <li>(555)7 210-4480</li>
      <li>rvalle@korvalen.com.ec</li>
      <li>www.korvalen.com.ec</li>
    </ul>
    <p class="letterhead-foot">Calle Olmedo e/ Sucre y Guayas, Portovelo - Ecuador EC070301</p>
  </section>

  <section class="piece envelope-front" aria-label="Sobre, frente">
    <div class="bars"><span class="bar-dark"></span><span class="bar-red"></span></div>
    <div class="brand">KORVALEN</div>
    <p class="envelope-address">Calle Olmedo e/ Sucre y Guayas, Portovelo - Ecuador EC070301</p>
    <ul class="contact">
      <li>(555)7 210-4480</li>
      <li>rvalle@korvalen.com.ec</li>
      <li>www.korvalen.com.ec</li>
    </ul>
  </section>

  <section class="piece envelope-back" aria-label="Sobre, reverso">
    <svg width="359" height="52" viewBox="0 0 359 52">
      <path d="M0 0H359V2C352 10 354 38 340 48Q336 52 328 52H31Q23 52 19 48C5 38 7 10 0 2Z" fill="var(--dark)"/>
    </svg>
  </section>

  <section class="piece card-front" aria-label="Tarjeta, frente">
    <div class="brand brand--light">KORVALEN</div>
    <p class="card-front-info">Calle Olmedo e/ Sucre y Guayas, Portovelo - Ecuador EC070301<br>(555)7 210-4480 | rvalle@korvalen.com.ec | www.korvalen.com.ec</p>
  </section>

  <section class="piece card-back" aria-label="Tarjeta, reverso">
    <div class="bars"><span class="bar-dark"></span><span class="bar-red"></span></div>
    <div class="brand">KORVALEN</div>
    <p class="card-person"><strong>ANDRÉS VALLE ORTIZ</strong>Gerente General</p>
    <div class="card-rule"></div>
    <ul class="contact contact--right">
      <li>(555)7 210-4480</li>
      <li>(555) 98 310-2277</li>
      <li>avalle@korvalen.com.ec</li>
      <li>www.korvalen.com.ec</li>
    </ul>
    <p class="card-back-address">Calle Olmedo e/ Sucre y Guayas, Portovelo - Ecuador EC070301</p>
  </section>

</body>
</html>
```